Beach Polo Event Flyer

The project consists of a flyer for a beach polo event that will occur on August 30 and 31

The flyer should contain the event details in spanish:
IV MARENQUA SHORE RIDING CUP
Hotel Varlowe
Agosto 30 y 31 2014
Horario: 2pm a 6pm
(Varlowe Logo)

Also contact info below:
info@brisadelvarclub.example
www.brisadelvarclub.example

A Space should be left on the bottom for us to add the sponsor logos when we have them.

The general idea is to do a flyer that looks elegant, inviting, inspired on the beach and the caribbean and shows the beauty of the sport and the beach.

I am attaching the flyer that a friend made that we DO NOT LIKE and some flyers from events in other parts of the world that we do like.
Also attached you will find the BRISADEL VAR CLUB logo which should go somewhere in the flyer. We are also attaching pictures from the past event in case you would need to use them.
We are open for any questions

```html
<!DOCTYPE html>
<html lang="es">
<head>
<meta charset="utf-8">
<title>IV Marenqua Shore Riding Cup</title>
<link rel="stylesheet" href="https://fonts.googleapis.com/css2?family=Cinzel:wght@600;700&family=Cormorant+Garamond:wght@500;600;700&family=Lato:wght@400&display=swap">
<style>
  :root {
    --navy: #1f3358;
    --gold: #c39a4e;
    --white: #ffffff;
    --sky-top: #2f6fc0;
    --sky-mid: #7fb0e0;
    --cloud: #e4eef7;
    --sea: #1f6796;
    --sand: #c7b08a;
    --sand-dark: #a8916c;
    --text-dark: #2a2f3a;
  }
  * { margin: 0; padding: 0; box-sizing: border-box; }
  html, body { width: 849px; height: 1200px; overflow: hidden; background: var(--white); }
  .flyer { position: relative; width: 849px; height: 1200px; background: var(--white); overflow: hidden; }

  .event-photo {
    position: absolute; left: 0; top: 0; width: 849px; height: 722px;
    background: linear-gradient(180deg,
      var(--sky-top) 0%, var(--sky-mid) 38%, var(--cloud) 52%,
      var(--sea) 57%, #3d86b0 64%,
      var(--sand) 68%, #bda57f 84%, var(--sand-dark) 100%);
  }
  .photo-rule { position: absolute; left: 0; top: 722px; width: 849px; height: 5px; background: var(--gold); }

  .club-badge {
    position: absolute; left: 600px; top: 0; width: 215px; height: 249px;
    background: var(--navy);
    display: flex; flex-direction: column; align-items: center; justify-content: center; gap: 18px;
  }
  .club-badge .badge-dot { width: 54px; height: 54px; border-radius: 50%; border: 2px solid var(--gold); }
  .club-badge .club-name {
    font-family: "Cinzel", serif; font-weight: 600; color: var(--gold);
    font-size: 20px; letter-spacing: 2px; text-align: center; line-height: 1.25;
  }

  .event-title {
    position: absolute; left: 0; top: 748px; width: 849px; text-align: center;
    font-family: "Cinzel", serif; font-weight: 700; color: var(--navy);
    font-size: 54px; line-height: 68px; letter-spacing: 1px;
  }
  .event-dates {
    position: absolute; left: 0; top: 900px; width: 849px;
    display: flex; align-items: center; justify-content: center; gap: 22px;
  }
  .event-dates .rule { width: 130px; height: 2px; background: var(--gold); }
  .event-dates .text {
    font-family: "Cinzel", serif; font-weight: 700; color: var(--gold);
    font-size: 27px; letter-spacing: 2px;
  }

  .event-venue {
    position: absolute; left: 0; top: 955px; width: 849px;
    display: flex; align-items: center; justify-content: center;
  }
  .event-venue .details {
    text-align: right; padding-right: 22px;
    font-family: "Cormorant Garamond", serif; font-weight: 600; color: var(--text-dark);
    font-size: 23px; line-height: 29px;
  }
  .event-venue .divider { width: 2px; height: 62px; background: var(--navy); }
  .event-venue .host {
    padding-left: 22px;
    font-family: "Cormorant Garamond", serif; font-weight: 700; color: var(--navy);
    font-size: 28px;
  }

  .sponsor-space { position: absolute; left: 0; top: 1030px; width: 849px; height: 128px; }

  .contact-bar {
    position: absolute; left: 0; top: 1158px; width: 849px; height: 42px;
    background: var(--navy); color: var(--white);
    display: flex; align-items: center; justify-content: center;
    font-family: "Lato", sans-serif; font-size: 15px; letter-spacing: 0.5px;
  }
  .contact-bar .sep { margin: 0 10px; }
</style>
</head>
<body>
  <main class="flyer">
    <div class="event-photo" role="img" aria-label="Polo riders on horseback playing on a sunny Caribbean beach with sea and blue sky behind"></div>
    <div class="photo-rule"></div>

    <div class="club-badge">
      <span class="badge-dot"></span>
      <p class="club-name">BRISADEL VAR<br>CLUB</p>
    </div>

    <h1 class="event-title">IV MARENQUA<br>SHORE RIDING CUP</h1>

    <div class="event-dates">
      <span class="rule"></span>
      <span class="text">AGOSTO 30 Y 31 2014</span>
      <span class="rule"></span>
    </div>

    <div class="event-venue">
      <div class="details">
        <p>at Hotel Varlowe</p>
        <p>Horario 2pm a 6pm</p>
      </div>
      <span class="divider"></span>
      <p class="host">Varlowe</p>
    </div>

    <div class="sponsor-space" aria-label="Reserved space for sponsor logos"></div>

    <footer class="contact-bar">
      <span>info@brisadelvarclub.example</span>
      <span class="sep">|</span>
      <span>www.brisadelvarclub.example</span>
    </footer>
  </main>
</body>
</html>
```